Harrowgate Supply Group Business Card Design

The Business Card will be one side only with Harrowgate Supplies Group Logo
Card should have:
Name
Title
Office phone Number
Cell Number
email address
Website
Street Address
Our Slogan is Rugged and Reliable
Looking for something that stands out from other business cards

Target Market(s)

Heavy equipment Lease Company

```html
<!DOCTYPE html>
<html lang="en">
<head>
<meta charset="utf-8">
<title>Harrowgate Supplies Group – Business Card</title>
<link rel="stylesheet" href="https://fonts.googleapis.com/css2?family=Montserrat:ital,wght@0,500;0,600;0,700;0,800;1,700&family=Roboto:wght@400;500&display=swap">
<style>
  :root {
    --backdrop: #1f1f1f;
    --navy: #2d2f80;
    --navy-deep: #262872;
    --red: #d92231;
    --white: #ffffff;
    --ink: #1d1d2b;
    --silver: #a3a5c4;
    --line: rgba(255,255,255,0.35);
  }
  * { margin: 0; padding: 0; box-sizing: border-box; }
  html, body { width: 1200px; height: 1200px; overflow: hidden; background: var(--backdrop); }
  body { position: relative; font-family: "Montserrat", sans-serif; }

  .card {
    position: absolute; left: 180px; width: 840px; height: 480px;
    border-radius: 22px; overflow: hidden;
    box-shadow: 0 14px 34px rgba(0,0,0,0.55);
  }

  /* Back of card */
  .card--back { top: 80px; background: linear-gradient(135deg, var(--navy-deep), #3a3c8e); }
  .back-brand {
    position: absolute; left: 0; right: 0; top: 50%; transform: translateY(-50%);
    display: flex; align-items: center; justify-content: center; gap: 22px;
  }
  .back-brand__dot { width: 46px; height: 46px; border-radius: 50%; background: var(--silver); }
  .back-brand__name {
    font-weight: 800; font-size: 46px; letter-spacing: 2px; color: var(--silver);
  }

  /* Front of card */
  .card--front { top: 620px; background: var(--white); }
  .front-waves { position: absolute; inset: 0; width: 840px; height: 480px; }

  .brand {
    position: absolute; top: 46px; left: 0; right: 0;
    display: flex; align-items: center; justify-content: center; gap: 16px;
  }
  .brand__dot { width: 40px; height: 40px; border-radius: 50%; background: var(--navy); }
  .brand__name { font-weight: 800; font-size: 38px; color: var(--red); letter-spacing: 0.5px; }

  .tagline {
    position: absolute; top: 104px; left: 0; right: 0; text-align: center;
    font-style: italic; font-weight: 700; font-size: 21px; color: var(--navy);
  }
  .tagline__accent { color: var(--red); }
  .tagline-rule {
    position: absolute; top: 140px; left: 399px; width: 42px; height: 3px; background: var(--red);
  }

  .person { position: absolute; top: 152px; left: 0; right: 0; text-align: center; }
  .person__name { font-weight: 800; font-size: 31px; color: var(--navy); line-height: 1.15; }
  .person__title { font-weight: 600; font-size: 19px; color: var(--red); margin-top: 2px; }
  .person__address { font-family: "Roboto", sans-serif; font-size: 17px; color: var(--ink); margin-top: 6px; }

  .contacts {
    position: absolute; top: 330px; left: 30px; width: 780px; height: 84px;
    display: grid; grid-template-columns: 1fr 1fr 1.4fr;
  }
  .contact {
    display: flex; flex-direction: column; align-items: center; justify-content: center; gap: 8px;
    color: var(--white); font-family: "Roboto", sans-serif; font-size: 19px; letter-spacing: 0.3px;
  }
  .contact + .contact { border-left: 1px solid var(--line); }
  .contact__icon {
    width: 38px; height: 38px; border: 2px solid var(--white); border-radius: 50%;
    display: flex; align-items: center; justify-content: center;
  }
  .contact__icon svg { width: 20px; height: 20px; }

  .website {
    position: absolute; right: 48px; bottom: 14px;
    font-family: "Roboto", sans-serif; font-size: 19px; color: var(--white); letter-spacing: 0.4px;
  }
</style>
</head>
<body>

  <section class="card card--back" aria-label="Card back">
    <div class="back-brand">
      <span class="back-brand__dot"></span>
      <span class="back-brand__name">HARROWGATE PUMPS</span>
    </div>
  </section>

  <section class="card card--front" aria-label="Card front">
    <svg class="front-waves" viewBox="0 0 840 480" preserveAspectRatio="none" aria-hidden="true">
      <!-- upper red swoosh -->
      <path d="M0 250 C 220 236, 430 292, 840 318 L 840 332 C 430 308, 220 262, 0 276 Z" fill="var(--red)"/>
      <!-- navy body -->
      <path d="M0 292 C 240 276, 440 326, 840 338 L 840 480 L 0 480 Z" fill="var(--navy)"/>
      <!-- thin red line inside navy top edge -->
      <path d="M300 306 C 500 334, 680 338, 840 336 L 840 341 C 680 343, 500 339, 300 310 Z" fill="var(--red)"/>
      <!-- bottom white + red sweep -->
      <path d="M0 432 C 250 450, 520 440, 840 428 L 840 480 L 0 480 Z" fill="var(--white)"/>
      <path d="M0 444 C 260 462, 520 452, 840 432 L 840 480 L 0 480 Z" fill="var(--red)"/>
      <path d="M440 450 C 600 440, 720 420, 840 400 L 840 436 C 700 452, 560 458, 440 450 Z" fill="var(--red)"/>
    </svg>

    <div class="brand">
      <span class="brand__dot"></span>
      <span class="brand__name">HARROWGATE SUPPLIES GROUP</span>
    </div>
    <p class="tagline">Rugged and <span class="tagline__accent">Reliable</span></p>
    <div class="tagline-rule"></div>

    <div class="person">
      <p class="person__name">Owen Castellan</p>
      <p class="person__title">Director of Sales &amp; Marketing</p>
      <p class="person__address">1400, 210 9 Avenue S.W, Calgary, AB, T2P 0K3</p>
    </div>

    <div class="contacts">
      <div class="contact">
        <span class="contact__icon">
          <svg viewBox="0 0 20 20" fill="none" stroke="#fff" stroke-width="1.6"><rect x="5" y="1.5" width="10" height="17" rx="1.8"/><rect x="7" y="4" width="6" height="5"/><path d="M7 12h1M10 12h1M13 12h-1M7 15h1M10 15h1M13 15h-1"/></svg>
        </span>
        <span>(587)555-0142</span>
      </div>
      <div class="contact">
        <span class="contact__icon">
          <svg viewBox="0 0 20 20" fill="#fff"><path d="M5 2l3 4-1.6 1.8c.9 2 2.4 3.6 4.4 4.6L12.6 11l4 3-1.8 2.6C9 16.4 3.6 11 3.4 5.2z"/></svg>
        </span>
        <span>(534)555-0176</span>
      </div>
      <div class="contact">
        <span class="contact__icon">
          <svg viewBox="0 0 20 20" fill="none" stroke="#fff" stroke-width="1.6"><rect x="2" y="4.5" width="16" height="11" rx="1"/><path d="M2 5l8 6.5L18 5M2 15l6-5M18 15l-6-5"/></svg>
        </span>
        <span>info@harrowgatesupplies.com</span>
      </div>
    </div>

    <p class="website">www.HarrowgatePumps.com</p>
  </section>

</body>
</html>
```